Torvalo PowerPoint Template

I have a company called Torvalo, LLC and my company logo is already designed. I need a PowerPoint template that I will be using to pitch potential investors and business partners. This should be a very professional-looking template that leverages the company logo colors and really pops. The company is an AI product research and development company.

```html
<!DOCTYPE html>
<html lang="en">
<head>
<meta charset="utf-8">
<title>Torvalo Presentation Template</title>
<link href="https://fonts.googleapis.com/css2?family=Inter+Tight:wght@500;600;700&family=Roboto:wght@400;500;700&display=swap" rel="stylesheet">
<style>
:root{
  --red:#c8202d;
  --ink:#3c3c3c;
  --dark:#4a4a4a;
  --grey:#8a8a8a;
  --light:#e4e4e4;
  --paper:#ffffff;
  --stage:#787878;
  --text:#6a6a6a;
}
*{box-sizing:border-box}
html,body{margin:0;width:1200px;height:746px;overflow:hidden;background:var(--stage)}
.slide{position:absolute;width:543px;height:305px;background:var(--paper);overflow:hidden;transform:scale(.4934);transform-origin:0 0;font-family:'Roboto',sans-serif;color:var(--ink)}
.abs{position:absolute}
.red{color:var(--red)}
.title{position:absolute;left:19px;top:12px;margin:0;font:600 21px/1 'Inter Tight',sans-serif;letter-spacing:-.8px;color:var(--ink)}
.brand{position:absolute;right:20px;top:11px;display:flex;align-items:center;gap:5px;font:600 22px/1 'Inter Tight',sans-serif;letter-spacing:-.6px;color:var(--red)}
.brand i{display:block;width:20px;height:20px;border-radius:50%;background:var(--red)}
.foot{position:absolute;left:19px;right:21px;bottom:7px;height:16px;display:flex;align-items:center}
.foot span{font-size:5.5px;color:var(--grey)}
.foot b{flex:1;height:1px;background:var(--red);margin:0 6px 0 14px}
.foot em{width:16px;height:16px;border:1px solid var(--red);border-radius:50%;font:normal 5.5px/14px 'Roboto',sans-serif;text-align:center;color:var(--red)}
.p{margin:0;font-size:6.5px;line-height:1.5;color:var(--text)}
.center{text-align:center}
.just{text-align:justify}
.h{margin:0;font:600 10.5px/1.2 'Roboto',sans-serif;color:var(--ink)}
.photo{position:absolute}
.card{position:absolute;background:#fff;border-radius:8px;box-shadow:0 2px 8px rgba(0,0,0,.15)}
.bar-head{position:absolute;height:27px;border-radius:3px 3px 0 0;color:#fff;font:600 9.5px/27px 'Roboto',sans-serif;text-align:center}
.dark-bg{background:var(--dark)}
.red-bg{background:var(--red)}
</style>
</head>
<body>

<!-- Row 1 -->
<section class="slide cover" style="left:28px;top:38px">
  <div class="brand" style="left:20px;right:auto;top:17px;font-size:28px"><i style="width:28px;height:28px"></i>Torvalo</div>
  <svg class="abs" style="left:0;top:0" width="543" height="305">
    <circle cx="397" cy="118" r="112" fill="var(--red)"/>
  </svg>
  <div class="photo" role="img" aria-label="Smiling senior couple portrait" style="left:200px;top:60px;width:343px;height:245px;background:linear-gradient(180deg,#d8c3a8 0%,#b99a7b 45%,#3b3f4f 100%);border-radius:150px 150px 0 0"></div>
  <h1 class="abs" style="left:19px;top:110px;margin:0;font:700 33px/1.15 'Inter Tight',sans-serif;letter-spacing:-1.2px"><span class="red">Presentation</span><br>Slide Title Here</h1>
  <svg class="abs" style="left:0;top:193px" width="260" height="8"><line x1="0" y1="4" x2="246" y2="4" stroke="var(--red)" stroke-width="2"/><circle cx="247" cy="4" r="3" fill="var(--red)"/></svg>
  <p class="abs" style="left:20px;top:213px;margin:0;font-size:10.5px">Your Subtitle Goes Here</p>
  <div class="abs" style="left:20px;top:243px;width:93px;height:23px;border:1.5px solid var(--red);border-radius:12px;font-size:7px;line-height:20px;text-align:center;color:var(--red)">MONTH XX, 2024</div>
</section>

<section class="slide" style="left:317px;top:38px">
  <h2 class="title"><span class="red">Title</span> Goes Here</h2>
  <div class="brand"><i></i>Torvalo</div>
  <svg class="abs" style="left:0;top:0" width="330" height="250" font-family="Roboto" font-size="5" fill="#555">
    <g stroke="#e6e6e6" stroke-width=".6">
      <line x1="45" y1="85" x2="300" y2="85"/><line x1="45" y1="110" x2="300" y2="110"/><line x1="45" y1="134" x2="300" y2="134"/><line x1="45" y1="159" x2="300" y2="159"/><line x1="45" y1="184" x2="300" y2="184"/><line x1="45" y1="208" x2="300" y2="208"/>
    </g>
    <line x1="45" y1="233" x2="300" y2="233" stroke="#999" stroke-width=".6"/>
    <text x="38" y="87">6</text><text x="38" y="112">5</text><text x="38" y="136">4</text><text x="38" y="161">3</text><text x="38" y="186">2</text><text x="38" y="210">1</text><text x="38" y="235">0</text>
    <g>
      <rect x="63" y="127" width="9" height="106" fill="var(--red)"/><rect x="74" y="176" width="9" height="57" fill="#777"/><rect x="85" y="184" width="9" height="49" fill="#1e1e1e"/>
      <rect x="127" y="127" width="9" height="106" fill="var(--red)"/><rect x="138" y="176" width="9" height="57" fill="#777"/><rect x="149" y="184" width="9" height="49" fill="#1e1e1e"/>
      <rect x="191" y="127" width="9" height="106" fill="var(--red)"/><rect x="202" y="176" width="9" height="57" fill="#777"/><rect x="213" y="184" width="9" height="49" fill="#1e1e1e"/>
      <rect x="256" y="127" width="9" height="106" fill="var(--red)"/><rect x="267" y="176" width="9" height="57" fill="#777"/><rect x="278" y="184" width="9" height="49" fill="#1e1e1e"/>
    </g>
    <text x="68" y="242">Category 1</text><text x="132" y="242">Category 1</text><text x="196" y="242">Category 1</text><text x="261" y="242">Category 1</text>
  </svg>
  <div class="abs" style="left:343px;top:63px;width:170px">
    <div style="display:flex;gap:9px;margin-bottom:16px"><span style="flex:none;width:11px;height:11px;border-radius:50%;background:var(--red);margin-top:1px"></span><div><h3 class="h">Title Goes Here</h3><p class="p just" style="font-size:5.8px;margin-top:3px">Lorem ipsum dolor sit amet, consectetur adipiscing elit, sed dolore magna aliqua. Ut enim exercitation ullamco laboris nisi ut aliquip ex ea commodo consequat.</p></div></div>
    <div style="display:flex;gap:9px;margin-bottom:16px"><span style="flex:none;width:11px;height:11px;border-radius:50%;background:#666;margin-top:1px"></span><div><h3 class="h">Title Goes Here</h3><p class="p just" style="font-size:5.8px;margin-top:3px">Lorem ipsum dolor sit amet, consectetur adipiscing elit, sed dolore magna aliqua. Ut enim exercitation ullamco laboris nisi ut aliquip ex ea commodo consequat.</p></div></div>
    <div style="display:flex;gap:9px"><span style="flex:none;width:11px;height:11px;border-radius:50%;background:#1e1e1e;margin-top:1px"></span><div><h3 class="h">Title Goes Here</h3><p class="p just" style="font-size:5.8px;margin-top:3px">Lorem ipsum dolor sit amet, consectetur adipiscing elit, sed dolore magna aliqua. Ut enim exercitation ullamco laboris nisi ut aliquip ex ea commodo consequat.</p></div></div>
  </div>
  <footer class="foot"><span>© 2025, Torvalo, LLC. All rights Reserved.</span><b></b><em>05</em></footer>
</section>

<section class="slide" style="left:607px;top:38px">
  <h2 class="title"><span class="red">Title</span> Goes Here</h2>
  <div class="brand"><i></i>Torvalo</div>
  <div class="card" style="left:19px;top:63px;width:118px;height:192px"></div>
  <div class="card" style="left:148px;top:63px;width:118px;height:192px"></div>
  <div class="card" style="left:276px;top:63px;width:118px;height:192px"></div>
  <div class="card" style="left:405px;top:63px;width:118px;height:192px"></div>
  <svg class="abs" style="left:0;top:0" width="543" height="305">
    <g fill="#9a8c82" stroke="var(--red)" stroke-width="2.5">
      <circle cx="78" cy="105" r="26"/><circle cx="207" cy="105" r="26"/><circle cx="335" cy="105" r="26"/><circle cx="464" cy="105" r="26"/>
    </g>
    <g fill="var(--dark)"><rect x="64" y="250" width="28" height="3"/><rect x="193" y="250" width="28" height="3"/><rect x="321" y="250" width="28" height="3"/><rect x="450" y="250" width="28" height="3"/></g>
  </svg>
  <div class="abs center" style="left:22px;top:142px;width:112px"><h3 class="h" style="font-size:8.5px;font-weight:500">Team Member Name</h3><p class="p" style="font-size:5.3px">Role/Position</p><p class="p" style="font-size:5.8px;margin-top:8px">Lorem ipsum dolor sit amet, consectetur adipiscing elit, sed do eiusmod tempor inci-minim veniam, quis nostrud exercitation ullamco laboris nisi ut ex sequat.</p></div>
  <div class="abs center" style="left:151px;top:142px;width:112px"><h3 class="h" style="font-size:8.5px;font-weight:500">Team Member Name</h3><p class="p" style="font-size:5.3px">Role/Position</p><p class="p" style="font-size:5.8px;margin-top:8px">Lorem ipsum dolor sit amet, consectetur adipiscing elit, sed do eiusmod tempor inci-minim veniam, quis nostrud exercitation ullamco laboris nisi ut ex sequat.</p></div>
  <div class="abs center" style="left:279px;top:142px;width:112px"><h3 class="h" style="font-size:8.5px;font-weight:500">Team Member Name</h3><p class="p" style="font-size:5.3px">Role/Position</p><p class="p" style="font-size:5.8px;margin-top:8px">Lorem ipsum dolor sit amet, consectetur adipiscing elit, sed do eiusmod tempor inci-minim veniam, quis nostrud exercitation ullamco laboris nisi ut ex sequat.</p></div>
  <div class="abs center" style="left:408px;top:142px;width:112px"><h3 class="h" style="font-size:8.5px;font-weight:500">Team Member Name</h3><p class="p" style="font-size:5.3px">Role/Position</p><p class="p" style="font-size:5.8px;margin-top:8px">Lorem ipsum dolor sit amet, consectetur adipiscing elit, sed do eiusmod tempor inci-minim veniam, quis nostrud exercitation ullamco laboris nisi ut ex sequat.</p></div>
  <div class="photo" role="img" aria-label="Team member portrait" style="display:none"></div>
  <footer class="foot"><span>© 2025, Torvalo, LLC. All rights Reserved.</span><b></b><em>09</em></footer>
</section>

<section class="slide" style="left:897px;top:38px">
  <h2 class="title"><span class="red">Title</span> Goes Here</h2>
  <div class="brand"><i></i>Torvalo</div>
  <h3 class="abs h" style="left:19px;top:77px;font-size:11.5px">Subtitle Goes Here</h3>
  <div class="abs" style="left:19px;top:103px;width:132px">
    <p class="p just" style="font-size:6px">Halvern Consulting is a consulting firm that specializes in providing its clients with comprehensive advice and support in the areas of strategy, marketing, communication, sales, distribution and product management.</p>
    <p class="p just" style="font-size:6px;margin-top:6px">Mara Halvern, founder and owner, has many years of experience as an executive in renowned Swiss companies in the luxury goods industry and has held numerous positions both in Switzerland and abroad.</p>
  </div>
  <div class="photo" role="img" aria-label="Portrait of a smiling senior executive in a suit" style="left:187px;top:55px;width:163px;height:205px;background:linear-gradient(160deg,#6b7480 0%,#3b4250 55%,#24262d 100%)"></div>
  <svg class="abs" style="left:367px;top:57px" width="50" height="190">
    <circle cx="24" cy="24" r="22" fill="var(--red)"/><circle cx="24" cy="94" r="22" fill="var(--dark)"/><circle cx="24" cy="163" r="22" fill="var(--red)"/>
    <g fill="none" stroke="#fff" stroke-width="1.4">
      <ellipse cx="24" cy="24" rx="9" ry="5"/><circle cx="24" cy="24" r="2.5"/>
      <circle cx="24" cy="94" r="9"/><circle cx="24" cy="94" r="5"/><circle cx="24" cy="94" r="1.5"/>
      <path d="M17 160 l7 9 l7 -9 l-3 -4 h-8z"/>
    </g>
  </svg>
  <div class="abs" style="left:425px;top:65px;width:100px"><h3 class="h" style="font-size:9.5px;font-weight:500">Title Goes Here</h3><p class="p" style="font-size:5.8px;margin-top:4px">Lorem ipsum dolor sit amet, consectetur adipiscing elit, sed dolore magna aliqua.</p></div>
  <div class="abs" style="left:425px;top:134px;width:100px"><h3 class="h" style="font-size:9.5px;font-weight:500">Title Goes Here</h3><p class="p" style="font-size:5.8px;margin-top:4px">Lorem ipsum dolor sit amet, consectetur adipiscing elit, sed dolore magna aliqua.</p></div>
  <div class="abs" style="left:425px;top:203px;width:100px"><h3 class="h" style="font-size:9.5px;font-weight:500">Title Goes Here</h3><p class="p" style="font-size:5.8px;margin-top:4px">Lorem ipsum dolor sit amet, consectetur adipiscing elit, sed dolore magna aliqua.</p></div>
  <footer class="foot"><span>© 2025, Torvalo, LLC. All rights Reserved.</span><b></b><em>13</em></footer>
</section>

<!-- Row 2 -->
<section class="slide" style="left:28px;top:211px">
  <div class="photo" role="img" aria-label="Businesswoman with a tablet by a city window" style="left:0;top:0;width:219px;height:305px;background:linear-gradient(160deg,#c5d3de 0%,#7f97ab 50%,#3d4e5f 100%)"></div>
  <h2 class="title" style="left:264px"><span class="red">Our</span> Agenda</h2>
  <div class="brand" style="font-size:17px"><i style="width:16px;height:16px"></i>Torvalo</div>
  <div class="abs" style="left:264px;top:57px;width:260px">
    <div class="agenda-row" style="display:flex;align-items:center;gap:14px;height:26px;margin-bottom:13.5px"><span style="width:22px;height:22px;clip-path:polygon(25% 0,75% 0,100% 50%,75% 100%,25% 100%,0 50%);background:var(--red);color:#fff;font-size:6.5px;line-height:22px;text-align:center">01</span><div style="flex:1;height:26px;box-shadow:0 1px 5px rgba(0,0,0,.15);border-right:3px solid var(--red);font:500 10px/26px 'Roboto',sans-serif;padding-left:16px">Introduction</div></div>
    <div style="display:flex;align-items:center;gap:14px;height:26px;margin-bottom:13.5px"><span style="width:22px;height:22px;clip-path:polygon(25% 0,75% 0,100% 50%,75% 100%,25% 100%,0 50%);background:var(--dark);color:#fff;font-size:6.5px;line-height:22px;text-align:center">02</span><div style="flex:1;height:26px;box-shadow:0 1px 5px rgba(0,0,0,.15);border-right:3px solid var(--dark);font:500 10px/26px 'Roboto',sans-serif;padding-left:16px">Our Team</div></div>
    <div style="display:flex;align-items:center;gap:14px;height:26px;margin-bottom:13.5px"><span style="width:22px;height:22px;clip-path:polygon(25% 0,75% 0,100% 50%,75% 100%,25% 100%,0 50%);background:var(--dark);color:#fff;font-size:6.5px;line-height:22px;text-align:center">03</span><div style="flex:1;height:26px;box-shadow:0 1px 5px rgba(0,0,0,.15);border-right:3px solid var(--dark);font:500 10px/26px 'Roboto',sans-serif;padding-left:16px">Statistics</div></div>
    <div style="display:flex;align-items:center;gap:14px;height:26px;margin-bottom:13.5px"><span style="width:22px;height:22px;clip-path:polygon(25% 0,75% 0,100% 50%,75% 100%,25% 100%,0 50%);background:var(--dark);color:#fff;font-size:6.5px;line-height:22px;text-align:center">04</span><div style="flex:1;height:26px;box-shadow:0 1px 5px rgba(0,0,0,.15);border-right:3px solid var(--dark);font:500 10px/26px 'Roboto',sans-serif;padding-left:16px">Graph</div></div>
    <div style="display:flex;align-items:center;gap:14px;height:26px;margin-bottom:13.5px"><span style="width:22px;height:22px;clip-path:polygon(25% 0,75% 0,100% 50%,75% 100%,25% 100%,0 50%);background:var(--dark);color:#fff;font-size:6.5px;line-height:22px;text-align:center">05</span><div style="flex:1;height:26px;box-shadow:0 1px 5px rgba(0,0,0,.15);border-right:3px solid var(--dark);font:500 10px/26px 'Roboto',sans-serif;padding-left:16px">Testimonial</div></div>
    <div style="display:flex;align-items:center;gap:14px;height:26px"><span style="width:22px;height:22px;clip-path:polygon(25% 0,75% 0,100% 50%,75% 100%,25% 100%,0 50%);background:var(--dark);color:#fff;font-size:6.5px;line-height:22px;text-align:center">06</span><div style="flex:1;height:26px;box-shadow:0 1px 5px rgba(0,0,0,.15);border-right:3px solid var(--dark);font:500 10px/26px 'Roboto',sans-serif;padding-left:16px">Contact Us</div></div>
  </div>
</section>

<section class="slide" style="left:317px;top:211px">
  <h2 class="title"><span class="red">Title</span> Goes Here</h2>
  <div class="brand"><i></i>Torvalo</div>
  <svg class="abs" style="left:0;top:0" width="543" height="200" font-family="Roboto">
    <g fill="none" stroke-width="9">
      <circle cx="116" cy="128" r="46" stroke="var(--light)"/>
      <circle cx="116" cy="128" r="46" stroke="#1a1a1a" stroke-dasharray="101 289" transform="rotate(-90 116 128)"/>
      <circle cx="271" cy="128" r="46" stroke="var(--light)"/>
      <circle cx="271" cy="128" r="46" stroke="var(--red)" stroke-dasharray="188 289" transform="rotate(-90 271 128)"/>
      <circle cx="426" cy="128" r="46" stroke="var(--light)"/>
      <circle cx="426" cy="128" r="46" stroke="var(--dark)" stroke-dasharray="246 289" transform="rotate(-90 426 128)"/>
    </g>
    <g font-size="16" font-weight="500" text-anchor="middle"><text x="116" y="134" fill="var(--ink)">35%</text><text x="271" y="134" fill="var(--red)">65%</text><text x="426" y="134" fill="var(--ink)">85%</text></g>
  </svg>
  <div class="abs center" style="left:51px;top:199px;width:130px"><h3 class="h" style="font-size:10px;font-weight:500">Heading Goes Here</h3><p class="p" style="font-size:5.8px;margin-top:4px">Lorem ipsum dolor sit amet, consectetur adipiscing elit, sed do eiusmod tempor incididunt ut labore et dolore magna enim ad minim aliqua.</p></div>
  <div class="abs center" style="left:206px;top:199px;width:130px"><h3 class="h red" style="font-size:10px;font-weight:500">Heading Goes Here</h3><p class="p" style="font-size:5.8px;margin-top:4px">Lorem ipsum dolor sit amet, consectetur adipiscing elit, sed do eiusmod tempor incididunt ut labore et dolore magna enim ad minim aliqua.</p></div>
  <div class="abs center" style="left:361px;top:199px;width:130px"><h3 class="h" style="font-size:10px;font-weight:500">Heading Goes Here</h3><p class="p" style="font-size:5.8px;margin-top:4px">Lorem ipsum dolor sit amet, consectetur adipiscing elit, sed do eiusmod tempor incididunt ut labore et dolore magna enim ad minim aliqua.</p></div>
  <footer class="foot"><span>© 2025, Torvalo, LLC. All rights Reserved.</span><b></b><em>06</em></footer>
</section>

<section class="slide" style="left:607px;top:211px">
  <svg class="abs" style="left:0;top:0" width="543" height="305"><circle cx="520" cy="165" r="240" fill="var(--red)"/></svg>
  <div class="photo" role="img" aria-label="Smiling senior couple" style="left:250px;top:55px;width:293px;height:250px;background:linear-gradient(180deg,#cdb7a3 0%,#8f7a6c 50%,#4a4a52 100%);border-radius:140px 140px 0 0"></div>
  <h2 class="title"><span class="red">Title</span> Goes Here</h2>
  <h3 class="abs h" style="left:19px;top:68px;font-size:13px;font-weight:500">Header Title Text Here</h3>
  <svg class="abs" style="left:0;top:91px" width="250" height="8"><line x1="0" y1="4" x2="243" y2="4" stroke="var(--red)" stroke-width="1.5"/><circle cx="244" cy="4" r="3" fill="var(--red)"/></svg>
  <div class="abs" style="left:19px;top:110px;width:230px">
    <p class="p just">Lorem ipsum dolor sit amet, consectetur adipiscing elit, sed do eiusmod tempor incididunt ut labore et dolore magna aliqua. Ut enim ad minim veniam, quis nostrud exercitation ullamco laboris nisi ut aliquip ex ea commodo consequat. Duis aute irure dolor in reprehenderit in voluptate velit esse cillum dolore eu fugiat nulla pariatur. Excepteur sint occaecat cupidatat non proident, sunt in culpa qui officia deserunt mollit anim id est laborum.</p>
    <p class="p just" style="margin-top:7px">Lorem ipsum dolor sit amet, consectetur adipiscing elit, sed do eiusmod tempor incididunt ut labore et dolore magna aliqua. Ut enim ad minim veniam, quis nostrud exercitation ullamco laboris nisi ut aliquip ex ea commodo consequat.</p>
  </div>
  <footer class="foot"><span>© 2025, Torvalo, LLC. All rights Reserved.</span><b></b><em>10</em></footer>
</section>

<section class="slide" style="left:897px;top:211px">
  <h2 class="title"><span class="red">Title</span> Goes Here</h2>
  <div class="brand"><i></i>Torvalo</div>
  <div class="card" style="left:31px;top:62px;width:152px;height:202px;border-radius:2px"></div>
  <div class="card" style="left:196px;top:62px;width:152px;height:202px;border-radius:2px"></div>
  <div class="card" style="left:360px;top:62px;width:152px;height:202px;border-radius:2px"></div>
  <div class="photo" role="img" aria-label="Friends sharing a meal at a table" style="left:31px;top:62px;width:152px;height:120px;background:linear-gradient(160deg,#8fa57a,#5d6f4a)"></div>
  <div class="photo" role="img" aria-label="Senior woman laughing with friends outdoors" style="left:196px;top:62px;width:152px;height:120px;background:linear-gradient(160deg,#b86a4c,#6d4a3e)"></div>
  <div class="photo" role="img" aria-label="Businessman in a warmly lit office" style="left:360px;top:62px;width:152px;height:120px;background:linear-gradient(160deg,#d08a3a,#3a3432)"></div>
  <div class="abs center" style="left:38px;top:194px;width:138px"><h3 class="h" style="font-size:9px;font-weight:500">TITLE GOES HERE</h3><p class="p" style="font-size:7px;margin-top:4px">Lorem ipsum dolor consectetur adipiscing elit, sed do eiusmod ut labore magna aliqua.</p></div>
  <div class="abs center" style="left:203px;top:194px;width:138px"><h3 class="h" style="font-size:9px;font-weight:500">TITLE GOES HERE</h3><p class="p" style="font-size:7px;margin-top:4px">Lorem ipsum dolor consectetur adipiscing elit, sed do eiusmod ut labore magna aliqua.</p></div>
  <div class="abs center" style="left:367px;top:194px;width:138px"><h3 class="h" style="font-size:9px;font-weight:500">TITLE GOES HERE</h3><p class="p" style="font-size:7px;margin-top:4px">Lorem ipsum dolor consectetur adipiscing elit, sed do eiusmod ut labore magna aliqua.</p></div>
  <footer class="foot"><span>© 2025, Torvalo, LLC. All rights Reserved.</span><b></b><em>14</em></footer>
</section>

<!-- Row 3 -->
<section class="slide" style="left:28px;top:384px">
  <h2 class="title"><span class="red">Who</span> We Are</h2>
  <div class="brand"><i></i>Torvalo</div>
  <svg class="abs" style="left:0;top:0" width="260" height="280"><circle cx="128" cy="162" r="107" fill="none" stroke="var(--red)" stroke-width="1.2"/><circle cx="128" cy="162" r="102" fill="none" stroke="var(--red)" stroke-width="1.2"/></svg>
  <div class="photo" role="img" aria-label="Colleagues shaking hands in a meeting room" style="left:32px;top:66px;width:192px;height:192px;border-radius:50%;background:linear-gradient(160deg,#a6aca8,#6b5d52 60%,#3d3530)"></div>
  <div class="abs" style="left:274px;top:68px;width:249px">
    <p class="p just">Lorem ipsum dolor sit amet, consectetur adipiscing elit, sed do eiusmod tempor incididunt ut labore et dolore magna aliqua. Ut enim ad minim veniam, quis nostrud exercitation ullamco laboris nisi ut aliquip ex ea commodo consequat. Duis aute irure dolor in reprehenderit in voluptate velit esse cillum dolore eu fugiat nulla pariatur. Excepteur sint occaecat cupidatat non proident, sunt in culpa qui officia deserunt mollit anim id est laborum.</p>
    <p class="p just" style="margin-top:9px">Sed ut perspiciatis unde omnis iste natus error sit voluptatem accusantium doloremque laudantium, totam rem aperiam, eaque ipsa quae ab illo inventore veritatis et quasi architecto beatae vitae dicta sunt explicabo. Nemo enim ipsam voluptatem quia voluptas sit aspernatur aut odit aut fugit, sed quia consequuntur magni dolores eos qui ratione voluptatem sequi nesciunt.</p>
  </div>
  <footer class="foot"><span>© 2025, Torvalo, LLC. All rights Reserved.</span><b></b><em>03</em></footer>
</section>

<section class="slide" style="left:317px;top:384px">
  <h2 class="title"><span class="red">Title</span> Goes Here</h2>
  <div class="brand"><i></i>Torvalo</div>
  <div class="abs center" style="left:132px;top:48px;width:100px"><h3 class="h red" style="font-size:8.5px;font-weight:500">Header Text here</h3><p class="p" style="font-size:5.8px;margin-top:3px">Lorem ipsum dolor sit amet, consectetur adipiscing elit, sed dolore magna aliqua.</p></div>
  <div class="abs center" style="left:310px;top:48px;width:100px"><h3 class="h red" style="font-size:8.5px;font-weight:500">Header Text here</h3><p class="p" style="font-size:5.8px;margin-top:3px">Lorem ipsum dolor sit amet, consectetur adipiscing elit, sed dolore magna aliqua.</p></div>
  <svg class="abs" style="left:0;top:0" width="543" height="305">
    <g fill="none" stroke-width="7">
      <circle cx="92" cy="162" r="44" stroke="var(--light)"/><circle cx="182" cy="162" r="44" stroke="var(--light)"/><circle cx="271" cy="162" r="44" stroke="var(--light)"/><circle cx="360" cy="162" r="44" stroke="var(--light)"/><circle cx="450" cy="162" r="44" stroke="var(--light)"/>
      <path d="M48 162 A44 44 0 0 1 136 162" stroke="var(--dark)"/>
      <path d="M138 162 A44 44 0 0 0 226 162" stroke="var(--red)"/>
      <path d="M227 162 A44 44 0 0 1 315 162" stroke="var(--dark)"/>
      <path d="M316 162 A44 44 0 0 0 404 162" stroke="var(--red)"/>
      <path d="M406 162 A44 44 0 0 1 494 162" stroke="var(--dark)"/>
    </g>
    <g fill="#fff" stroke="#ddd" stroke-width="1"><circle cx="92" cy="162" r="17"/><circle cx="182" cy="162" r="17"/><circle cx="271" cy="162" r="17"/><circle cx="360" cy="162" r="17"/><circle cx="450" cy="162" r="17"/></g>
    <g fill="none" stroke="#777" stroke-width="1.2">
      <rect x="85" y="154" width="14" height="10"/><line x1="92" y1="164" x2="92" y2="170"/>
      <circle cx="182" cy="158" r="4" stroke="var(--red)"/><path d="M175 170 q7 -8 14 0" stroke="var(--red)"/>
      <rect x="264" y="154" width="14" height="12"/><path d="M267 162 l3 -3 l3 2 l3 -4"/>
      <rect x="352" y="155" width="7" height="6" stroke="var(--red)"/><rect x="362" y="163" width="7" height="6" stroke="var(--red)"/>
      <circle cx="450" cy="162" r="6"/><circle cx="450" cy="162" r="2"/>
    </g>
    <g fill="#fff" stroke="var(--red)" stroke-width="1.3"><circle cx="137" cy="162" r="4"/><circle cx="226" cy="162" r="4"/><circle cx="316" cy="162" r="4" stroke="#555"/><circle cx="405" cy="162" r="4"/><circle cx="494" cy="162" r="4"/></g>
  </svg>
  <div class="abs center" style="left:42px;top:226px;width:100px"><h3 class="h" style="font-size:8.5px;font-weight:500">Header Text here</h3><p class="p" style="font-size:5.8px;margin-top:3px">Lorem ipsum dolor sit amet, consectetur adipiscing elit, sed dolore magna aliqua.</p></div>
  <div class="abs center" style="left:221px;top:226px;width:100px"><h3 class="h" style="font-size:8.5px;font-weight:500">Header Text here</h3><p class="p" style="font-size:5.8px;margin-top:3px">Lorem ipsum dolor sit amet, consectetur adipiscing elit, sed dolore magna aliqua.</p></div>
  <div class="abs center" style="left:400px;top:226px;width:100px"><h3 class="h" style="font-size:8.5px;font-weight:500">Header Text here</h3><p class="p" style="font-size:5.8px;margin-top:3px">Lorem ipsum dolor sit amet, consectetur adipiscing elit, sed dolore magna aliqua.</p></div>
  <footer class="foot"><span>© 2025, Torvalo, LLC. All rights Reserved.</span><b></b><em>07</em></footer>
</section>

<section class="slide" style="left:607px;top:384px">
  <h2 class="title"><span class="red">Title</span> Goes Here</h2>
  <div class="brand"><i></i>Torvalo</div>
  <div class="bar-head dark-bg" style="left:19px;top:64px;width:240px">Header Text Here</div>
  <div class="bar-head red-bg" style="left:283px;top:64px;width:240px">Header Text Here</div>
  <div class="abs" style="left:19px;top:103px;width:240px"><p class="p just" style="font-size:6px">Lorem ipsum dolor sit amet, consectetur adipiscing elit, do eiusmod tempor incididunt ut labore et dolore magna aliqua. Ut enim ad minim veniam, quis nostrud exercitation ullamco laboris nisi ut aliquip ex ea commodo consequat. Duis aute irure dolor in reprehenderit in voluptate velit esse cillum dolore eu fugiat nulla pariatur. Excepteur sint occaecat cupidatat non proident, sunt in culpa qui officia deserunt mollit anim id est laborum.</p><p class="p just" style="font-size:6px;margin-top:6px">Sed ut perspiciatis unde omnis iste natus error sit voluptatem accusantium doloremque laudantium, totam rem aperiam, eaque ipsa quae ab illo inventore veritatis et quasi architecto beatae vitae dicta sunt explicabo. Nemo enim ipsam voluptatem quia voluptas sit aspernatur aut odit aut fugit, sed quia consequuntur magni dolores eos qui ratione voluptatem sequi nesciunt. Neque porro quisquam est, qui dolorem ipsum quia dolor sit amet, incidunt ut labore et dolore magnam aliquam quaerat voluptatem.</p></div>
  <div class="abs" style="left:283px;top:103px;width:240px"><p class="p just" style="font-size:6px">Lorem ipsum dolor sit amet, consectetur adipiscing elit, do eiusmod tempor incididunt ut labore et dolore magna aliqua. Ut enim ad minim veniam, quis nostrud exercitation ullamco laboris nisi ut aliquip ex ea commodo consequat. Duis aute irure dolor in reprehenderit in voluptate velit esse cillum dolore eu fugiat nulla pariatur. Excepteur sint occaecat cupidatat non proident, sunt in culpa qui officia deserunt mollit anim id est laborum.</p><p class="p just" style="font-size:6px;margin-top:6px">Sed ut perspiciatis unde omnis iste natus error sit voluptatem accusantium doloremque laudantium, totam rem aperiam, eaque ipsa quae ab illo inventore veritatis et quasi architecto beatae vitae dicta sunt explicabo. Nemo enim ipsam voluptatem quia voluptas sit aspernatur aut odit aut fugit, sed quia consequuntur magni dolores eos qui ratione voluptatem sequi nesciunt. Neque porro quisquam est, qui dolorem ipsum quia dolor sit amet, incidunt ut labore et dolore magnam aliquam quaerat voluptatem.</p></div>
  <footer class="foot"><span>© 2025, Torvalo, LLC. All rights Reserved.</span><b></b><em>11</em></footer>
</section>

<section class="slide" style="left:897px;top:384px">
  <h2 class="title"><span class="red">Title</span> Goes Here</h2>
  <div class="brand"><i></i>Torvalo</div>
  <svg class="abs" style="left:0;top:0" width="543" height="305" font-family="Roboto" text-anchor="middle">
    <rect x="122" y="82" width="116" height="17" fill="var(--dark)"/><rect x="241" y="82" width="116" height="17" fill="var(--red)"/><rect x="360" y="82" width="117" height="17" fill="var(--dark)"/>
    <g fill="#fff" font-size="6.5" font-weight="500"><text x="180" y="93">Text Here</text><text x="299" y="93">Text Here</text><text x="418" y="93">Text Here</text></g>
    <rect x="64" y="97" width="20" height="146" fill="var(--dark)"/>
    <g fill="#f0f0f0"><rect x="98" y="104" width="379" height="21"/><rect x="98" y="151" width="379" height="21"/><rect x="98" y="198" width="379" height="21"/></g>
    <g fill="var(--ink)" font-size="5"><text x="180" y="117">Add Contents Title</text><text x="299" y="117">Add Contents Title</text><text x="418" y="117">Add Contents Title</text>
    <text x="180" y="141">Add Contents Title</text><text x="299" y="141">Add Contents Title</text><text x="418" y="141">Add Contents Title</text>
    <text x="180" y="164">Add Contents Title</text><text x="299" y="164">Add Contents Title</text><text x="418" y="164">Add Contents Title</text>
    <text x="180" y="188">Add Contents Title</text><text x="299" y="188">Add Contents Title</text><text x="418" y="188">Add Contents Title</text>
    <text x="180" y="211">Add Contents Title</text><text x="299" y="211">Add Contents Title</text><text x="418" y="211">Add Contents Title</text></g>
    <g fill="none" stroke="#fff" stroke-width="1.2"><circle cx="74" cy="114" r="5"/><rect x="69" y="133" width="10" height="8"/><rect x="69" y="156" width="10" height="9"/><circle cx="74" cy="180" r="3"/><path d="M69 189 q5 -6 10 0"/><circle cx="74" cy="207" r="5"/></g>
  </svg>
  <footer class="foot"><span>© 2025, Torvalo, LLC. All rights Reserved.</span><b></b><em>15</em></footer>
</section>

<!-- Row 4 -->
<section class="slide" style="left:28px;top:557px">
  <h2 class="title"><span class="red">Our</span> Services</h2>
  <div class="brand"><i></i>Torvalo</div>
  <svg class="abs" style="left:0;top:0" width="543" height="305">
    <g fill="none" stroke="#555" stroke-width="1"><path d="M202 102 h12 v18 h30"/><path d="M341 102 h-12 v18 h-30"/><path d="M202 222 h12 v-18 h30"/><path d="M341 222 h-12 v-18 h-30"/></g>
  </svg>
  <div class="card" style="left:31px;top:58px;width:157px;height:87px;border-radius:3px"></div>
  <div class="card" style="left:355px;top:58px;width:157px;height:87px;border-radius:3px"></div>
  <div class="card" style="left:31px;top:177px;width:157px;height:87px;border-radius:3px"></div>
  <div class="card" style="left:355px;top:177px;width:157px;height:87px;border-radius:3px"></div>
  <div class="card" style="left:222px;top:112px;width:100px;height:100px;border-radius:50%"></div>
  <div class="brand" style="left:236px;right:auto;top:154px;font-size:13px;gap:4px"><i style="width:11px;height:11px"></i>Torvalo</div>
  <svg class="abs" style="left:0;top:0" width="543" height="305">
    <g fill="var(--red)"><circle cx="190" cy="102" r="12"/><circle cx="355" cy="102" r="12"/><circle cx="190" cy="222" r="12"/><circle cx="355" cy="222" r="12"/></g>
    <g fill="none" stroke="#fff" stroke-width="1.1"><circle cx="190" cy="102" r="5"/><rect x="350" y="97" width="10" height="10"/><rect x="185" y="217" width="10" height="10"/><path d="M350 227 l10 -10 M350 217 l10 10"/></g>
  </svg>
  <div class="abs center" style="left:40px;top:66px;width:125px"><h3 class="h" style="font-size:8.5px;font-weight:500">Lorem ipsum dolor amet, consectetur adipiscing</h3><p class="p" style="font-size:5.8px;margin-top:6px">Ut enim minim veniam, quis nostrud exercitation ullamco laboris aliquip commodo consequat.</p></div>
  <div class="abs center" style="left:373px;top:66px;width:125px"><h3 class="h" style="font-size:8.5px;font-weight:500">Lorem ipsum dolor amet, consectetur adipiscing</h3><p class="p" style="font-size:5.8px;margin-top:6px">Ut enim minim veniam, quis nostrud exercitation ullamco laboris aliquip commodo consequat.</p></div>
  <div class="abs center" style="left:40px;top:185px;width:125px"><h3 class="h" style="font-size:8.5px;font-weight:500">Lorem ipsum dolor amet, consectetur adipiscing</h3><p class="p" style="font-size:5.8px;margin-top:6px">Ut enim minim veniam, quis nostrud exercitation ullamco laboris aliquip commodo consequat.</p></div>
  <div class="abs center" style="left:373px;top:185px;width:125px"><h3 class="h" style="font-size:8.5px;font-weight:500">Lorem ipsum dolor amet, consectetur adipiscing</h3><p class="p" style="font-size:5.8px;margin-top:6px">Ut enim minim veniam, quis nostrud exercitation ullamco laboris aliquip commodo consequat.</p></div>
  <footer class="foot"><span>© 2025, Torvalo, LLC. All rights Reserved.</span><b></b><em>04</em></footer>
</section>

<section class="slide" style="left:317px;top:557px">
  <h2 class="title"><span class="red">Title</span> Goes Here</h2>
  <div class="brand"><i></i>Torvalo</div>
  <svg class="abs" style="left:0;top:0" width="543" height="305">
    <rect x="0" y="106" width="100" height="8" fill="var(--dark)"/><rect x="100" y="106" width="172" height="8" fill="var(--red)"/><rect x="272" y="106" width="172" height="8" fill="var(--dark)"/><rect x="444" y="106" width="99" height="8" fill="#9a9a9a"/>
    <g fill="#fff" stroke-width="1.5"><circle cx="99" cy="110" r="40" stroke="var(--dark)"/><circle cx="272" cy="110" r="40" stroke="var(--red)"/><circle cx="446" cy="110" r="40" stroke="var(--dark)"/></g>
    <g stroke-width="1"><line x1="99" y1="150" x2="99" y2="177" stroke="var(--dark)"/><line x1="272" y1="150" x2="272" y2="177" stroke="var(--red)"/><line x1="446" y1="150" x2="446" y2="177" stroke="var(--dark)"/></g>
    <g><circle cx="99" cy="178" r="2" fill="var(--dark)"/><circle cx="272" cy="178" r="2" fill="var(--red)"/><circle cx="446" cy="178" r="2" fill="var(--dark)"/></g>
    <g fill="none" stroke-width="1.3">
      <circle cx="99" cy="102" r="8" stroke="var(--dark)"/><path d="M84 112 q8 14 15 14 q7 0 15 -14" stroke="var(--dark)"/>
      <rect x="257" y="97" width="30" height="20" stroke="var(--red)"/><line x1="272" y1="117" x2="272" y2="124" stroke="var(--red)"/><line x1="264" y1="124" x2="280" y2="124" stroke="var(--red)"/>
      <path d="M432 126 v-16 h12 v-6 h16 v22 z" stroke="var(--dark)"/><path d="M438 94 l-4 -4 M454 94 l4 -4 M446 92 v-6" stroke="var(--dark)"/>
    </g>
  </svg>
  <div class="abs center" style="left:24px;top:190px;width:150px"><h3 class="h" style="font-size:9.5px;font-weight:500">Lorem ipsum sit amet</h3><p class="p" style="margin-top:6px">Lorem ipsum dolor sit amet, consectetur adipiscing elit, sed do eiusmod tempor incididunt ut labore et dolore magna ad minim veniam, quis aliqua.</p></div>
  <div class="abs center" style="left:197px;top:190px;width:150px"><h3 class="h red" style="font-size:9.5px;font-weight:500">Lorem ipsum sit amet</h3><p class="p" style="margin-top:6px">Lorem ipsum dolor sit amet, consectetur adipiscing elit, sed do eiusmod tempor incididunt ut labore et dolore magna ad minim veniam, quis aliqua.</p></div>
  <div class="abs center" style="left:371px;top:190px;width:150px"><h3 class="h" style="font-size:9.5px;font-weight:500">Lorem ipsum sit amet</h3><p class="p" style="margin-top:6px">Lorem ipsum dolor sit amet, consectetur adipiscing elit, sed do eiusmod tempor incididunt ut labore et dolore magna ad minim veniam, quis aliqua.</p></div>
  <footer class="foot"><span>© 2025, Torvalo, LLC. All rights Reserved.</span><b></b><em>07</em></footer>
</section>

<section class="slide" style="left:607px;top:557px">
  <h2 class="title"><span class="red">Title</span> Goes Here</h2>
  <div class="brand"><i></i>Torvalo</div>
  <div class="bar-head dark-bg" style="left:19px;top:69px;width:153px">Header Text Here</div>
  <div class="bar-head red-bg" style="left:195px;top:69px;width:153px">Header Text Here</div>
  <div class="bar-head dark-bg" style="left:370px;top:69px;width:153px">Header Text Here</div>
  <svg class="abs" style="left:0;top:0" width="543" height="305"><g stroke="#ddd" stroke-width=".8"><line x1="183" y1="106" x2="183" y2="255"/><line x1="359" y1="106" x2="359" y2="255"/></g></svg>
  <div class="abs" style="left:19px;top:107px;width:153px"><p class="p" style="font-size:5.8px">Lorem ipsum dolor sit amet, consectetur adipiscing elit, do eiusmod tempor incididunt ut labore et dolore magna aliqua. Ut enim ad minim veniam, quis nostrud exercitation ullamco laboris nisi ut aliquip ex ea commodo consequat. Duis aute irure dolor in reprehenderit in voluptate velit esse cillum dolore eu fugiat nulla pariatur.</p><p class="p" style="font-size:5.8px;margin-top:6px">Sed ut perspiciatis unde omnis iste natus error sit voluptatem accusantium doloremque laudantium, totam rem aperiam, eaque ipsa quae ab illo inventore veritatis et quasi architecto beatae vitae dicta sunt explicabo. Nemo enim ipsam voluptatem quia voluptas sit aspernatur voluptatem sequi nesciunt.</p></div>
  <div class="abs" style="left:195px;top:107px;width:153px"><p class="p" style="font-size:5.8px">Lorem ipsum dolor sit amet, consectetur adipiscing elit, do eiusmod tempor incididunt ut labore et dolore magna aliqua. Ut enim ad minim veniam, quis nostrud exercitation ullamco laboris nisi ut aliquip ex ea commodo consequat. Duis aute irure dolor in reprehenderit in voluptate velit esse cillum dolore eu fugiat nulla pariatur.</p><p class="p" style="font-size:5.8px;margin-top:6px">Sed ut perspiciatis unde omnis iste natus error sit voluptatem accusantium doloremque laudantium, totam rem aperiam, eaque ipsa quae ab illo inventore veritatis et quasi architecto beatae vitae dicta sunt explicabo. Nemo enim ipsam voluptatem quia voluptas sit aspernatur voluptatem sequi nesciunt.</p></div>
  <div class="abs" style="left:370px;top:107px;width:153px"><p class="p" style="font-size:5.8px">Lorem ipsum dolor sit amet, consectetur adipiscing elit, do eiusmod tempor incididunt ut labore et dolore magna aliqua. Ut enim ad minim veniam, quis nostrud exercitation ullamco laboris nisi ut aliquip ex ea commodo consequat. Duis aute irure dolor in reprehenderit in voluptate velit esse cillum dolore eu fugiat nulla pariatur.</p><p class="p" style="font-size:5.8px;margin-top:6px">Sed ut perspiciatis unde omnis iste natus error sit voluptatem accusantium doloremque laudantium, totam rem aperiam, eaque ipsa quae ab illo inventore veritatis et quasi architecto beatae vitae dicta sunt explicabo. Nemo enim ipsam voluptatem quia voluptas sit aspernatur voluptatem sequi nesciunt.</p></div>
  <footer class="foot"><span>© 2025, Torvalo, LLC. All rights Reserved.</span><b></b><em>12</em></footer>
</section>

<section class="slide" style="left:897px;top:557px">
  <div class="abs red-bg" style="left:291px;top:0;width:252px;height:305px"></div>
  <div class="brand" style="left:30px;right:auto;top:28px;font-size:30px;gap:7px"><i style="width:31px;height:31px"></i>Torvalo</div>
  <h2 class="abs" style="left:30px;top:135px;margin:0;font:600 33px/1 'Inter Tight',sans-serif;letter-spacing:-1.2px">Thank <span class="red">You</span></h2>
  <svg class="abs" style="left:0;top:0" width="543" height="305">
    <g fill="var(--dark)"><circle cx="291" cy="47" r="25"/><circle cx="291" cy="131" r="25"/><circle cx="291" cy="216" r="25"/></g>
    <g fill="none" stroke="#fff" stroke-width="1.6">
      <path d="M283 38 q-2 6 4 14 q6 7 12 6 l2 -4 l-5 -3 l-2 2 q-5 -3 -7 -8 l2 -2 l-2 -5 z" fill="#fff"/>
      <circle cx="291" cy="131" r="11"/><ellipse cx="291" cy="131" rx="5" ry="11"/><line x1="280" y1="131" x2="302" y2="131"/>
      <rect x="280" y="209" width="22" height="15"/><path d="M280 209 l11 9 l11 -9"/>
    </g>
  </svg>
  <div class="abs" style="left:330px;top:35px;color:#fff"><p style="margin:0;font-size:7px">Phone Number</p><p style="margin:4px 0 0;font:600 11px 'Roboto',sans-serif">+1 (555) 014-2290</p></div>
  <div class="abs" style="left:330px;top:119px;color:#fff"><p style="margin:0;font-size:7px">Website</p><p style="margin:4px 0 0;font:600 11px 'Roboto',sans-serif">www.torvalollc.com/</p></div>
  <div class="abs" style="left:330px;top:204px;color:#fff"><p style="margin:0;font-size:7px">E-mail Address</p><p style="margin:4px 0 0;font:600 11px 'Roboto',sans-serif">info@torvalollc.com</p></div>
</section>

</body>
</html>
```